FLYER DESIGN FOR COMPUTER GIVEAWAY

I need a flyer designed for a Promotion I am running for my business.

I am giving away prizes in return for customers to register their details with us. The clients just need to goto www.brightlinetech.com.au/promo and register their details (Name, Email, mobile etc) to go in the draw to win these prizes.

1st Prize is a Desktop Computer package (24 Inch Monitor, Tower, Keyboard, Mouse)
2nd Prize is a Laptop (Possibly an QV or ORVO)
3rd Prize is a 24 inch Computer monitor

and many other giveaways such as Printers, computer speakers, usb flash drives etc

The flyer needs to have our logo on it (sample found on the website. Once the design is chosen, I will provide PSD logo).

The Flyer needs to be very eye catchy and attractive with its colours and design in general. When someone sees it among other flyers they will be inclined to pick it up and read it...

The design needs to be unique and very creative.

Please submit your designs only if you can fulfill the requirements above.

Information required on the Flyer:

Visit brightlinetech.com.au/promo and enter your details before June 30th for your chance to win.
(This sentence can be reworded if needed)

Runner up prizes include Printers, computer speakers, usb flash drives

One application per person

Please design on A5 size.

Below are some images to stimulate some ideas:
http://www.pixmarrow.com/stock-illustration-40293817-christmas-surprise.php?st=c73d209

http://drawvault.net/wp-content/uploads/2012/04/exploding-gift-box-objects.png

http://image.frametrove.com/display_pic_with_logo/57018/57018,1947520316,3/stock-vector-exploding-gift-box-with-music-elements-82746105.jpg

NOTE: The idea of an exploding gift box with lots of prizes coming out of it with lots of colours (as can be seen from the sample images above) will be highly desirable.

Target Market(s)

Home owners.

Industry/Entity Type

Computer

Requirements
Must have
• Must be very attractive and creative design
Must be a unique design
Should not have
• design should not have dull or bland colours.

```html
<!DOCTYPE html>
<html lang="en">
<head>
<meta charset="utf-8">
<title>Brightline Tech Promotion Flyer</title>
<link rel="stylesheet" href="https://fonts.googleapis.com/css2?family=Luckiest+Guy&family=Arimo:wght@400;700&family=Russo+One&display=swap">
<style>
  :root {
    --orange-core: #f79a22;
    --orange-edge: #e64b2a;
    --brown: #7a3a10;
    --brown-deep: #5a2708;
    --cream: #fde9b8;
    --glow: #ffd23a;
    --navy: #2b2a72;
    --badge-blue: #2a3fa0;
    --badge-light: #5d7fe0;
    --white: #ffffff;
    --band: rgba(255, 200, 180, 0.6);
    --warn-yellow: #ffe23a;
    --tag-purple: #5a3fb0;
  }
  * { box-sizing: border-box; margin: 0; padding: 0; }
  html, body { width: 863px; height: 1200px; overflow: hidden; background: var(--orange-edge); }
  .flyer {
    position: relative;
    width: 863px;
    height: 1200px;
    overflow: hidden;
    background: radial-gradient(ellipse 70% 60% at 50% 42%, var(--orange-core) 0%, #f27a22 55%, var(--orange-edge) 100%);
    font-family: "Arimo", Arial, sans-serif;
  }
  .headline {
    position: absolute;
    left: 0; width: 100%;
    text-align: center;
    font-family: "Luckiest Guy", "Arial Black", sans-serif;
    font-weight: 400;
    letter-spacing: 1px;
    line-height: 1;
  }
  .headline--visit {
    top: 54px;
    font-size: 54px;
    color: #b4561b;
    -webkit-text-stroke: 2px var(--brown-deep);
    text-shadow: 0 0 6px var(--glow), 0 0 10px var(--glow), 2px 3px 0 var(--brown-deep);
  }
  .headline--enter {
    top: 206px; left: -20px;
    font-size: 42px;
    color: var(--brown);
    -webkit-text-stroke: 1px var(--brown-deep);
    text-shadow: 0 0 4px var(--cream), 0 0 7px var(--cream), 2px 2px 0 var(--cream);
  }
  .headline--chance {
    top: 256px; left: -20px;
    font-size: 44px;
    color: var(--brown);
    text-shadow: 0 0 4px var(--white), 0 0 8px var(--white), 2px 2px 0 var(--white);
  }
  .headline--win {
    top: 306px; left: -20px;
    font-size: 42px;
    color: var(--white);
    -webkit-text-stroke: 2px var(--brown);
    text-shadow: 2px 3px 0 var(--brown-deep);
  }
  .url-bar {
    position: absolute;
    left: 48px; top: 113px;
    width: 678px; height: 62px;
    border-radius: 14px;
    background: linear-gradient(#5a5f6e, #2f323b);
    padding: 6px;
  }
  .url-bar__field {
    width: 100%; height: 100%;
    border-radius: 10px;
    background: linear-gradient(#ffffff, #dfe1e6);
    display: flex; align-items: center; justify-content: center;
    font-size: 34px;
    color: #43454d;
    letter-spacing: -0.3px;
    white-space: nowrap;
  }
  .go-button {
    position: absolute;
    left: 739px; top: 113px;
    width: 72px; height: 68px;
    border-radius: 12px;
    background: linear-gradient(#6e5da8, #3b2e70);
    border: 2px solid #2a1f55;
    color: var(--white);
    font-size: 42px;
    font-weight: 700;
    display: flex; align-items: center; justify-content: center;
  }
  .deadline-tag {
    position: absolute;
    left: 618px; top: 236px;
    width: 190px; height: 175px;
    transform: rotate(-17deg);
  }
  .tag-string { position: absolute; left: 720px; top: 175px; }
  .prize-badge {
    position: absolute;
    width: 94px; height: 94px;
    border-radius: 50%;
    background: radial-gradient(circle at 50% 30%, var(--badge-light), var(--badge-blue) 70%);
    border: 4px solid var(--white);
    box-shadow: 0 4px 10px rgba(90, 30, 0, 0.4);
    color: var(--white);
    text-align: center;
  }
  .prize-badge__rank {
    display: block;
    margin-top: 6px;
    font-size: 50px;
    font-weight: 700;
    line-height: 1;
  }
  .prize-badge__rank sup { font-size: 16px; vertical-align: 26px; }
  .prize-badge__label { display: block; font-size: 15px; font-weight: 700; margin-top: 2px; }
  .prize-text {
    position: absolute;
    color: var(--navy);
    font-size: 20px;
    line-height: 1.28;
    white-space: nowrap;
  }
  .prize-text__title { font-weight: 700; display: block; }
  .product-shot {
    position: absolute;
    border-radius: 10px;
  }
  .product-shot--dark { background: linear-gradient(160deg, #3a3d44, #0e0f12); }
  .product-shot--print { background: linear-gradient(160deg, #c8cad0, #4c5058); }
  .product-shot--usb { background: linear-gradient(160deg, #d23a3a, #7d3fa8 60%, #2a2a30); }
  .runner-heading {
    position: absolute;
    top: 858px; left: 0; width: 100%;
    text-align: center;
    color: var(--white);
    font-size: 35px;
    font-weight: 400;
  }
  .runner-label {
    position: absolute;
    top: 1058px;
    font-family: "Russo One", "Arial Black", sans-serif;
    color: var(--white);
    font-size: 17px;
    letter-spacing: 1px;
    text-align: center;
  }
  .giveaways {
    position: absolute;
    top: 1098px; left: 0; width: 100%;
    text-align: center;
    color: var(--white);
    font-size: 26px;
  }
  .notice-band {
    position: absolute;
    left: 17px; top: 1140px;
    width: 825px; height: 43px;
    background: var(--band);
    border: 1px solid rgba(255, 255, 255, 0.5);
  }
  .notice-band__text {
    position: absolute;
    left: 88px; top: 6px;
    font-family: "Russo One", "Arial Black", sans-serif;
    font-size: 24px;
    letter-spacing: 2.6px;
    color: var(--white);
    white-space: nowrap;
  }
  .notice-icon { position: absolute; left: 22px; top: 1128px; }
</style>
</head>
<body>
<main class="flyer">
  <h1 class="headline headline--visit">Visit our website</h1>

  <div class="url-bar"><div class="url-bar__field">www.brightlinetech.com.au/promo</div></div>
  <div class="go-button">GO</div>

  <svg class="tag-string" width="60" height="100" viewBox="0 0 60 100">
    <path d="M18 4 C 5 40, 10 70, 40 96" fill="none" stroke="#3a2a20" stroke-width="2"/>
  </svg>

  <h2 class="headline headline--enter">Enter your details</h2>
  <p class="headline headline--chance">For a chance</p>
  <p class="headline headline--win">TO WIN!</p>

  <svg class="deadline-tag" viewBox="0 0 200 185">
    <defs>
      <linearGradient id="tagFace" x1="0" y1="0" x2="0" y2="1">
        <stop offset="0" stop-color="#e4e6ea"/>
        <stop offset="1" stop-color="#a9adb4"/>
      </linearGradient>
      <radialGradient id="clockFace" cx="0.5" cy="0.4" r="0.6">
        <stop offset="0" stop-color="#f2f2ff"/>
        <stop offset="1" stop-color="#9c8fe0"/>
      </radialGradient>
    </defs>
    <rect x="0" y="0" width="200" height="185" rx="6" fill="url(#tagFace)" stroke="#7d8088"/>
    <circle cx="100" cy="12" r="5" fill="#5a5d64"/>
    <text x="100" y="40" text-anchor="middle" font-family="Arimo, Arial, sans-serif" font-weight="700" font-size="24" fill="#8d9097">BEFORE</text>
    <circle cx="100" cy="93" r="40" fill="#ffffff" stroke="#c9cbd0" stroke-width="3"/>
    <circle cx="100" cy="93" r="33" fill="url(#clockFace)"/>
    <line x1="100" y1="93" x2="100" y2="66" stroke="#5a3fb0" stroke-width="3" stroke-linecap="round"/>
    <line x1="100" y1="93" x2="88" y2="112" stroke="#3a8ee0" stroke-width="3" stroke-linecap="round"/>
    <rect x="20" y="145" width="160" height="32" rx="4" fill="var(--tag-purple)"/>
    <text x="100" y="169" text-anchor="middle" font-family="Arimo, Arial, sans-serif" font-weight="700" font-size="21" fill="#ffffff">30<tspan font-size="13" dy="-7">th</tspan><tspan dy="7"> JUNE</tspan></text>
  </svg>

  <section class="prizes">
    <div class="prize-badge" style="left:75px; top:496px;"><span class="prize-badge__rank">1<sup>st</sup></span><span class="prize-badge__label">PRIZE</span></div>
    <p class="prize-text" style="left:188px; top:509px;"><span class="prize-text__title">Desktop Computer package</span>(24 Inch Monitor,Tower,<br>Keyboard and mouse.)</p>
    <div class="product-shot product-shot--dark" style="left:482px; top:433px; width:225px; height:154px;" role="img" aria-label="Desktop computer package with monitor, tower, keyboard and mouse"></div>

    <div class="prize-badge" style="left:139px; top:617px;"><span class="prize-badge__rank">2<sup>nd</sup></span><span class="prize-badge__label">PRIZE</span></div>
    <p class="prize-text" style="left:248px; top:642px;"><span class="prize-text__title">Laptop</span>(Possibly an QV or ORVO)</p>
    <div class="product-shot product-shot--dark" style="left:500px; top:616px; width:211px; height:87px;" role="img" aria-label="Two laptop computers"></div>

    <div class="prize-badge" style="left:88px; top:747px;"><span class="prize-badge__rank">3<sup>rd</sup></span><span class="prize-badge__label">PRIZE</span></div>
    <p class="prize-text" style="left:197px; top:772px;"><span class="prize-text__title">Computer monitor</span>24 inch</p>
    <div class="product-shot product-shot--dark" style="left:403px; top:721px; width:285px; height:126px;" role="img" aria-label="Two widescreen computer monitors"></div>
  </section>

  <h2 class="runner-heading">Runner up prizes include</h2>

  <div class="product-shot product-shot--print" style="left:43px; top:914px; width:231px; height:134px;" role="img" aria-label="Inkjet printers"></div>
  <div class="product-shot product-shot--dark" style="left:322px; top:919px; width:255px; height:130px;" role="img" aria-label="Computer speaker sets"></div>
  <div class="product-shot product-shot--usb" style="left:596px; top:923px; width:241px; height:125px;" role="img" aria-label="Assorted USB flash drives"></div>

  <p class="runner-label" style="left:43px; width:231px;">Printers</p>
  <p class="runner-label" style="left:312px; width:275px;">Computer Speakers</p>
  <p class="runner-label" style="left:596px; width:241px;">USB Flash Drives</p>

  <p class="giveaways">And many, many other giveaways...</p>

  <div class="notice-band"><p class="notice-band__text">Only one application allowed per person.</p></div>
  <svg class="notice-icon" width="60" height="60" viewBox="0 0 60 60">
    <circle cx="30" cy="30" r="27" fill="var(--warn-yellow)" stroke="#ffffff" stroke-width="3"/>
    <rect x="26" y="12" width="8" height="24" rx="4" fill="#3a2a10"/>
    <circle cx="30" cy="45" r="4.5" fill="#3a2a10"/>
  </svg>
</main>
</body>
</html>
```